Business card for Drone Aerial

I need a business card designed keeping in mind I want to do post cards also with a similar design.
Both sides of the card would be cool.
I have a vortel 8 max and would like a picture of it on the front of the card. Similar to one I attached.
I really like the look of a drone in the air and the background pic a little blurry. I attached a few images as IDEAS.
Some special things I want to be on the card additional to the normal business card info:
"Aerial Photography" or "Low Altitude Aerial Photography"?
"KTO# 58203917"

I like modern and creative. My Favorite color is blue and I like blue on white.
I do not have a business name and am not going to have one. When they read "Aerial Photography" and see the drone and image they will know what the card is for.

FYI, The attached pictures are just images from pixelgrove and just samples/ideas.

Target Market(s)

Real estate, construction, events

Industry/Entity Type

Business

Contact Information for Business Card

Also Definitely want to contain, my name, my number and email address.

Requirements
Must have
• "KTO# 58203917"
• "Aerial Photography"

```html
<!DOCTYPE html>
<html lang="en">
<head>
<meta charset="utf-8">
<title>Aerial Photography – Business Card</title>
<link href="https://fonts.googleapis.com/css2?family=Tinos:wght@400&family=Ubuntu:wght@400&family=Arimo:wght@400&display=swap" rel="stylesheet">
<style>
  :root {
    --backdrop: #e9ebee;
    --card-white: #f7f7f7;
    --ink: #111111;
    --navy: #0e1238;
    --navy-line: #1b2a6b;
    --blue: #1f6fb5;
    --sky-top: #4f86c9;
    --sky-mid: #b9d3ea;
    --ground: #6f8f6a;
    --text-light: #ffffff;
  }
  * { box-sizing: border-box; margin: 0; padding: 0; }
  html, body { width: 1200px; height: 902px; overflow: hidden; }
  body {
    background: var(--backdrop);
    display: flex;
    flex-direction: column;
    align-items: center;
    justify-content: center;
    gap: 44px;
  }
  .card {
    position: relative;
    width: 680px;
    height: 389px;
    overflow: hidden;
    box-shadow: 0 4px 14px rgba(0,0,0,0.18);
  }

  /* Back side */
  .card-back {
    background: var(--card-white);
    display: flex;
    flex-direction: column;
    align-items: center;
    justify-content: center;
    gap: 18px;
  }
  .card-back .title {
    font-family: "Tinos", serif;
    font-weight: 400;
    font-size: 60px;
    line-height: 1;
    color: var(--ink);
    letter-spacing: 1px;
    white-space: nowrap;
  }
  .card-back .rule {
    width: 420px;
    height: 3px;
    background: var(--ink);
  }

  /* Front side */
  .card-front { background: var(--blue); }
  .card-front .panels { position: absolute; inset: 0; }
  .card-front .title {
    position: absolute;
    right: 30px;
    top: 62px;
    font-family: "Tinos", serif;
    font-weight: 400;
    font-size: 38px;
    line-height: 1.2;
    color: var(--text-light);
    white-space: nowrap;
  }
  .contact {
    position: absolute;
    right: 26px;
    top: 200px;
    text-align: right;
    color: var(--text-light);
  }
  .contact .name {
    font-family: "Ubuntu", sans-serif;
    font-size: 24px;
    margin-bottom: 14px;
  }
  .contact .line {
    font-family: "Arimo", sans-serif;
    font-size: 15px;
    display: flex;
    justify-content: flex-end;
    align-items: center;
    gap: 8px;
    margin-bottom: 6px;
  }
  .contact .license { margin-top: 10px; margin-right: 20px; }
  .contact .icon { width: 12px; height: 12px; flex: none; }
</style>
</head>
<body>

  <section class="card card-back" aria-label="Card back">
    <h1 class="title">Aerial Photography</h1>
    <div class="rule" aria-hidden="true"></div>
  </section>

  <section class="card card-front" aria-label="Card front">
    <svg class="panels" viewBox="0 0 680 389">
      <defs>
        <linearGradient id="photoTone" x1="0" y1="0" x2="0" y2="1">
          <stop offset="0" stop-color="var(--sky-top)"/>
          <stop offset="0.5" stop-color="var(--sky-mid)"/>
          <stop offset="0.85" stop-color="var(--ground)"/>
          <stop offset="1" stop-color="#e8e4d8"/>
        </linearGradient>
      </defs>
      <polygon points="190,0 680,0 680,175 395,175" fill="var(--navy)"/>
      <polygon role="img" aria-label="Photo of a drone flying above a beachfront city skyline"
               points="0,0 175,0 385,180 385,389 0,389" fill="url(#photoTone)"/>
      <polyline points="175,0 385,180 385,389" fill="none" stroke="var(--navy-line)" stroke-width="6"/>
    </svg>

    <h2 class="title">Aerial Photography</h2>

    <div class="contact">
      <p class="name">Dariel Voskanyan</p>
      <p class="line">021 5093 7714
        <svg class="icon" viewBox="0 0 12 12" aria-hidden="true"><rect x="0.5" y="0.5" width="11" height="11" rx="1.5" fill="#fff"/><path d="M3.5 3h1.5l.6 1.6-.9.7c.4.8 1 1.4 1.8 1.8l.7-.9 1.6.6V8.5c0 .3-.3.5-.6.5C5.4 9 3 6.6 3 3.6c0-.3.2-.6.5-.6z" fill="var(--blue)"/></svg>
      </p>
      <p class="line">dariel@skyframeaerial.com
        <svg class="icon" viewBox="0 0 12 12" aria-hidden="true"><rect x="0.5" y="0.5" width="11" height="11" rx="1.5" fill="#fff"/><rect x="2.5" y="3.5" width="7" height="5" fill="none" stroke="var(--blue)"/><path d="M2.5 3.5l3.5 3 3.5-3" fill="none" stroke="var(--blue)"/></svg>
      </p>
      <p class="line license">KTO# 58203917</p>
    </div>
  </section>

</body>
</html>
```